eBook opt in for website

I write short ebooks (2500 words) to give free as an opt in. I need a cover design with block headers within the pages to highlight the specifics sections for PDF.
Book Title:
Bridgeway Mentoring
Sharpen Your Crew Guidance Using Five Simple Habits
I would like to see a design for the front cover that would emphasize a leader's personal growth to team.
The color that comes to mind is blue.
I do have a Brand Design and Icon if you need it.

Leaders with Team Responsibility
Business Consultant

```html
<!DOCTYPE html>
<html lang="en">
<head>
<meta charset="UTF-8">
<title>Bridgeway Mentoring – eBook Cover</title>
<link rel="stylesheet" href="https://fonts.googleapis.com/css2?family=Oswald:wght@600&family=Rokkitt:wght@300&family=Josefin+Sans:wght@400&display=swap">
<style>
  :root {
    --page-bg: #f2f2f2;
    --cover-blue: #2f9fd3;
    --scene-light: #4bb3de;
    --scene-mid: #2e8fc0;
    --scene-deep: #1f79a8;
    --title-cyan: #52f6ff;
    --subtitle-cream: #f4f39a;
    --accent-green: #45f25e;
  }
  * { margin: 0; padding: 0; box-sizing: border-box; }
  html, body {
    width: 1200px;
    height: 1000px;
    overflow: hidden;
    background: var(--page-bg);
  }
  .canvas {
    position: relative;
    width: 1200px;
    height: 1000px;
  }
  .cover {
    position: absolute;
    left: 297px;
    top: 97px;
    width: 605px;
    height: 806px;
    background: var(--cover-blue);
    overflow: hidden;
  }
  .cover-title {
    position: absolute;
    left: 0;
    top: 40px;
    width: 100%;
    text-align: center;
    font-family: "Oswald", sans-serif;
    font-weight: 600;
    font-size: 104px;
    line-height: 142px;
    letter-spacing: 9px;
    color: var(--title-cyan);
    text-transform: uppercase;
  }
  .cover-title span { display: block; }
  .team-scene {
    position: absolute;
    left: 0;
    top: 353px;
    width: 100%;
    height: 453px;
    background: linear-gradient(180deg, var(--scene-light) 0%, var(--scene-mid) 55%, var(--scene-deep) 100%);
  }
  .cover-subtitle {
    position: absolute;
    left: 0;
    top: 395px;
    width: 100%;
    text-align: center;
    font-family: "Rokkitt", serif;
    font-weight: 300;
    font-size: 42px;
    color: var(--subtitle-cream);
  }
  .cover-subtitle .line {
    display: block;
    height: 112px;
    line-height: 112px;
    white-space: nowrap;
  }
  .cover-subtitle .habit-count {
    font-family: "Josefin Sans", sans-serif;
    font-weight: 400;
    font-size: 76px;
    color: var(--accent-green);
    vertical-align: -12px;
    margin: 0 6px;
  }
</style>
</head>
<body>
  <div class="canvas">
    <div class="cover">
      <div class="team-scene" role="img" aria-label="Photo of a business team standing in silhouette before tall office windows, tinted blue"></div>
      <h1 class="cover-title">
        <span>Bridgeway</span>
        <span>Mentoring</span>
      </h1>
      <p class="cover-subtitle">
        <span class="line">Sharpen Your</span>
        <span class="line">Crew Guidance</span>
        <span class="line">Using <span class="habit-count">Five</span> Simple Habits</span>
      </p>
    </div>
  </div>
</body>
</html>
```